We need a brand new Employee Handbook for a team of aged and disability support workers

We need an employee handbook designed for our team of aged and disability support workers.
We provide a range of disability and aged care services to persons in our region.
We are a small business, providing unique and personalised support to vulnerable people. We actually provide choice and control to our clients - something the bigger agencies say they do but don't follow through with.
We aim to be an employer of choice - providing a workplace that supports our staff personally and professionally.
We would like to see the colours gold, yellow, black, grey and white.
We would like to incorporate photos of our current team members and stock photos of fun teams, persons with a disability, elderly and carers in the community and home.
The final design should communicate a fun, supportive team offering growth and opportunity.

```html
<!DOCTYPE html>
<html lang="en">
<head>
<meta charset="utf-8">
<title>Brightway Care – Induction Guide</title>
<link rel="stylesheet" href="https://fonts.googleapis.com/css2?family=Archivo:wght@400;600;700;900&display=swap">
<style>
:root{
  --bg:#dcdcdd;
  --paper:#ffffff;
  --paper-soft:#efefef;
  --ink:#3a3a3a;
  --ink-dark:#1d1d1d;
  --grey:#8d8d8d;
  --grey-light:#b5b5b5;
  --gold:#c9ae3c;
  --gold-light:#e3d27a;
  --gold-dark:#a98e22;
  --band:#6f6f6f;
}
*{box-sizing:border-box;margin:0;padding:0}
html,body{width:1200px;height:2317px;overflow:hidden}
body{background:var(--bg);font-family:"Archivo",Arial,sans-serif;color:var(--ink);position:relative}
.page{position:absolute;width:480px;height:340px;background:var(--paper);overflow:hidden;box-shadow:0 6px 18px rgba(0,0,0,.12)}
.spread{position:absolute;left:120px;width:960px;height:340px}
.spread .page{top:0}
.spread .page.left{left:0}
.spread .page.right{left:480px}
.spread::after{content:"";position:absolute;left:470px;top:0;width:20px;height:340px;background:linear-gradient(90deg,transparent,rgba(0,0,0,.10),transparent);pointer-events:none}

.brand{position:absolute;font-weight:700;color:var(--gold);font-size:19px;letter-spacing:.2px;white-space:nowrap}
.pill{position:absolute;border-radius:20px;background:linear-gradient(90deg,var(--gold-dark),var(--gold-light) 60%,var(--gold));color:var(--ink-dark);display:flex;align-items:center}
.photo{position:absolute}

/* cover */
.cover-title{position:absolute;left:36px;top:92px;font-weight:900;font-size:44px;line-height:1;color:var(--ink);letter-spacing:-1px;white-space:nowrap;z-index:2}
.cover-pill{left:36px;top:248px;width:226px;height:36px;padding:0 14px;font-size:10px;line-height:1.2;justify-content:space-between;z-index:2}
.cover-photo{right:0;top:0;width:40%;height:100%;background:linear-gradient(160deg,#cfd6df,#d9a98c 45%,#c9645f 70%,#aab3c3)}

/* welcome */
.welcome-page{background:var(--paper-soft)}
.welcome-title{position:absolute;left:34px;top:178px;font-weight:900;font-size:56px;color:var(--ink-dark);letter-spacing:-1px;white-space:nowrap}
.welcome-pill{left:40px;top:248px;width:250px;height:22px;font-size:9px;font-weight:600;padding-left:14px}
.welcome-circle{left:300px;top:52px;width:120px;height:120px;border-radius:50%;background:radial-gradient(circle at 40% 40%,#5fb5e6,#1f7fc0)}
.acknowledge{position:absolute;left:34px;bottom:20px;width:410px;font-size:6.5px;font-weight:700;color:var(--ink);line-height:1.3}
.toc-photo{left:0;top:0;width:200px;height:100%;background:linear-gradient(150deg,#2d2d2d,#7a5a3e 50%,#cfcfcf)}
.toc{position:absolute;left:222px;top:36px}
.toc-kicker{font-size:22px;color:var(--grey-light);font-weight:400;line-height:1}
.toc-head{font-size:30px;color:var(--grey);font-weight:900;line-height:1}
.toc-rule{width:40px;height:4px;background:var(--grey);margin:8px 0 12px}
.toc-list{list-style:none;font-size:7.5px;line-height:1.55;color:var(--ink)}
.toc-list li span{display:inline-block;width:18px}
.toc-sub{padding-left:30px;font-size:6.5px;color:var(--grey)}

/* pledge */
.pledge-text{position:absolute;left:34px;top:70px;width:200px}
.pledge-title{font-size:17px;line-height:1.15;font-weight:400;color:var(--ink-dark)}
.pledge-title strong{font-weight:900}
.pledge-body{margin-top:12px;font-size:7.5px;line-height:1.45}
.pledge-body p{margin-bottom:6px}
.pledge-photo{left:250px;top:0;width:230px;height:100%;background:linear-gradient(160deg,#e9e3da,#c8a887 45%,#8b96a8)}
.footer-band{position:absolute;left:0;bottom:18px;height:14px;background:var(--band);color:#fff;font-size:6.5px;display:flex;align-items:center;padding-left:26px}
.director-photo{left:30px;top:44px;width:140px;height:140px;background:linear-gradient(180deg,#d6d6d6,#7b7b7b);border:5px solid #f4f4f4;box-shadow:0 0 0 1px #ddd}
.director-pill{left:46px;top:198px;width:110px;height:20px;font-size:7px;font-weight:700;justify-content:center}
.director-role{position:absolute;left:46px;top:222px;width:110px;text-align:center;font-size:6.5px;line-height:1.4;color:var(--grey)}
.message{position:absolute;left:194px;top:40px;width:260px}
.message h2{font-size:19px;font-weight:900;color:var(--gold);line-height:1.1}
.message .lead{margin-top:8px;font-size:9.5px;line-height:1.35;color:var(--ink-dark);font-weight:600}
.message .small{margin-top:8px;font-size:6.5px;line-height:1.5;color:var(--ink)}
.message .sign{margin-top:6px;font-size:7px}
.page-no{position:absolute;right:20px;bottom:18px;width:22px;height:14px;background:var(--band);color:#fff;font-size:6.5px;display:flex;align-items:center;justify-content:center}

/* back cover */
.back-photo{left:0;top:0;width:100%;height:236px;background:linear-gradient(180deg,#2a2a2a,#1b1b1b)}
.back-tab{position:absolute;left:155px;top:194px;width:170px;height:70px;border-radius:85px 85px 0 0;background:var(--paper);display:flex;align-items:flex-start;justify-content:center;padding-top:22px}
.back-tab .brand{position:static;font-size:16px}
.contacts{position:absolute;left:0;right:0;top:284px;display:flex;justify-content:center;gap:18px;font-size:7.5px;color:var(--ink)}
.contacts span{display:flex;align-items:center;gap:4px}
</style>
</head>
<body>

<!-- cover -->
<section class="page cover" style="left:360px;top:134px">
  <div class="brand" style="left:36px;top:36px">Brightway Care</div>
  <h1 class="cover-title">Induction<br>Guide</h1>
  <div class="pill cover-pill">A practical guide to your<br>employment journey
    <svg width="40" height="10" viewBox="0 0 40 10"><path d="M0 5H36M31 1l5 4-5 4" stroke="#1d1d1d" stroke-width="1.4" fill="none"/></svg>
  </div>
  <div class="photo cover-photo" role="img" aria-label="Team members stacking hands together"></div>
</section>

<!-- welcome + contents -->
<section class="spread" style="top:700px">
  <div class="page left welcome-page">
    <div class="photo welcome-circle" role="img" aria-label="Cheerful older man in a green jumper"></div>
    <h2 class="welcome-title">Welcome!</h2>
    <div class="pill welcome-pill">WE'RE GLAD TO HAVE YOU ON BOARD.</div>
    <p class="acknowledge">We acknowledge the traditional owners of the land we work on – the Ngunnawal people – and pay our respect to their Elders both past and present.</p>
  </div>
  <div class="page right">
    <div class="photo toc-photo" role="img" aria-label="Colleagues working together at a laptop"></div>
    <div class="toc">
      <div class="toc-kicker">TABLE OF</div>
      <div class="toc-head">CONTENT</div>
      <div class="toc-rule"></div>
      <ul class="toc-list">
        <li><span>01.</span>EMPLOYER PLEDGE</li>
        <li><span>02.</span>MESSAGE FROM DIRECTOR</li>
        <li><span>03.</span>INTRODUCTION</li>
        <li><span>04.</span>OUR STORY</li>
        <li><span>05.</span>OUR MISSION</li>
        <li><span>06.</span>OUR VALUES</li>
        <li><span>07.</span>OUR GOALS</li>
        <li class="toc-sub">a) ORGANISATIONAL STRUCTURE</li>
        <li class="toc-sub">b) YOUR TEAM</li>
        <li class="toc-sub">c) YOUR ROLE</li>
        <li class="toc-sub">d) YOUR TRAINING PLAN</li>
        <li class="toc-sub">e) POLICIES</li>
        <li class="toc-sub">f) ONBOARDING CHECKLIST</li>
        <li class="toc-sub">g) SYSTEMS &amp; TOOLS</li>
      </ul>
    </div>
  </div>
</section>

<!-- pledge + director -->
<section class="spread" style="top:1250px">
  <div class="page left">
    <div class="pledge-text">
      <h2 class="pledge-title">Our pledge to be an<br><strong>'Employer of Choice'</strong></h2>
      <div class="pledge-body">
        <p>We care about you! You matter. Your family and those who care for you matter.</p>
        <p>Your emotional, physical, spiritual and psychological needs are important to us. Giving you opportunity for professional and personal growth is important to us.</p>
        <p>Giving you opportunity for training, skill development and career progression is important to us.</p>
        <p>We will listen to you. We will give you constructive feedback.</p>
        <p>We will support you based on your needs and goals.</p>
        <p>Your wellbeing inspires us to grow, learn and improve.</p>
      </div>
    </div>
    <div class="photo pledge-photo" role="img" aria-label="Young support worker writing at a desk"></div>
    <div class="footer-band" style="width:250px">www.brightwaycare.com.au</div>
  </div>
  <div class="page right">
    <div class="photo director-photo" role="img" aria-label="Black and white portrait of the director"></div>
    <div class="pill director-pill">MARA ELLIS</div>
    <div class="director-role">Director<br>Brightway Care</div>
    <div class="message">
      <h2>Message from the<br>Director</h2>
      <p class="lead">Welcome to Brightway Care! We are thrilled to have you join our team. We do some amazing, exciting &amp; challenging work here, and we are hopeful that your talent, enthusiasm, and fresh ideas will help take us to a new level!</p>
      <p class="small">We hope that you find this handbook useful. We welcome any suggestions and questions you may have – please don't hesitate to ask. Every day you will make a real difference to the people we support. We look forward to growing together and to your contribution to our commitment to genuine choice and control at the heart of everything we do. We hope you enjoy this journey as much as we will.</p>
      <p class="sign">- Mara</p>
    </div>
    <div class="footer-band" style="width:230px">www.brightwaycare.com.au</div>
    <div class="page-no">04</div>
  </div>
</section>

<!-- back + front cover -->
<section class="spread" style="top:1820px">
  <div class="page left">
    <div class="photo back-photo" role="img" aria-label="Dark toned photo of a team gathering"></div>
    <div class="back-tab"><span class="brand">Brightway Care</span></div>
    <div class="contacts">
      <span><svg width="8" height="8" viewBox="0 0 10 10"><path d="M2 1h2l1 2-1.2 1a6 6 0 0 0 2.2 2.2L7 5l2 1v2c-4 .5-8-3.5-7-7z" fill="#c9ae3c"/></svg>0400 000 000</span>
      <span><svg width="7" height="9" viewBox="0 0 10 13"><path d="M5 0a5 5 0 0 1 5 5c0 3-5 8-5 8S0 8 0 5a5 5 0 0 1 5-5z" fill="#c9ae3c"/><circle cx="5" cy="5" r="2" fill="#fff"/></svg>12 Wattle Lane RIVERTON NSW 2000</span>
      <span><svg width="9" height="7" viewBox="0 0 12 9"><rect width="12" height="9" rx="1" fill="#c9ae3c"/><path d="M0 1l6 4 6-4" stroke="#fff" fill="none"/></svg>hello@brightwaycare.com.au</span>
      <span><svg width="8" height="8" viewBox="0 0 10 10"><circle cx="5" cy="5" r="5" fill="#c9ae3c"/></svg>www.brightwaycare.com.au</span>
    </div>
  </div>
  <div class="page right cover">
    <div class="brand" style="left:36px;top:36px">Brightway Care</div>
    <h1 class="cover-title">Induction<br>Guide</h1>
    <div class="pill cover-pill">A practical guide to your<br>employment journey
      <svg width="40" height="10" viewBox="0 0 40 10"><path d="M0 5H36M31 1l5 4-5 4" stroke="#1d1d1d" stroke-width="1.4" fill="none"/></svg>
    </div>
    <div class="photo cover-photo" role="img" aria-label="Team members stacking hands together"></div>
  </div>
</section>

</body>
</html>
```